Book Cover Design "WHEN PATIENT MONEY MEETS A CAREFULLY TIMED PLAN"

I need somebody to design a book cover for my book

The title is ...
"WHEN PATIENT MONEY MEETS A CAREFULLY TIMED PLAN"

The sub title is ...
"A simple step-by-step guide to buying the best shares at the best time written specifically for non-professional investors."

The book is 5 inches by 8 inches and we are looking for a cover design. However we will need a high resolution design so we can create large posters and banners etc, We also need the cover to stand out when viewed on Parcelora etc.

The back of the book must have in large writing...
"A book about the stock market for people who don't read books about the stock market."
The back of the book must have in smaller writing...
"An easy to follow, easy to read book, outlining a 15 step process to help you make better investing decisions."

Please don't use a lot or red. The color red signifies losses in the stock market. Please use blue as the dominant color.

Our website is not live yet, but please visit http://brookvalesaverinstitute.plinkdev.uk/ if you want an idea of how its going to look when it goes live. We would be receptive if you design the cover and back cover in the same brand image as the website.

However, please feel free to design what you like, we are open to anything.

Anybody who invests in stocks and shares as a hobby or in any none-professional capacity.

Finance

85cae6
85acd3
0255a3
3277b5
85abd2
cfdeed
cee9f5
33a6d7
0292cd

• A front and back cover!
• A copy of our company logo on the front and back.
• The price of the book on the back (The price is £15.99)
• The ISBN Bar code for 978-1000472913
• Authors name "Desmond Pelham" on the front
• If you could have "Published by the Brookvale Saver Institute" somewhere on the back in small writing, and also the website if possible?
• www.brookvale-saver-institute.com

```html
<!DOCTYPE html>
<html lang="en">
<head>
<meta charset="utf-8">
<title>Back Cover – A book about the stock market</title>
<link rel="stylesheet" href="https://fonts.googleapis.com/css2?family=Barlow+Condensed:wght@500;600&family=Roboto:ital,wght@1,400;1,700&display=swap">
<style>
  :root {
    --cover-blue: #0b6fbf;
    --quote-navy: #1f3873;
    --highlight-yellow: #f6d53c;
    --text-white: #ffffff;
    --corner-white: #ffffff;
    --imprint-ink: #23262b;
  }
  html, body {
    margin: 0;
    padding: 0;
    overflow: hidden;
    background: var(--cover-blue);
  }
  .back-cover {
    position: relative;
    width: 751px;
    height: 1200px;
    background: var(--cover-blue);
    overflow: hidden;
  }
  .headline {
    position: absolute;
    left: 81px;
    top: 158px;
    margin: 0;
    font-family: "Barlow Condensed", sans-serif;
    font-weight: 600;
    font-size: 88px;
    line-height: 84px;
    letter-spacing: -0.5px;
    color: var(--text-white);
  }
  .headline .line { display: block; }
  .headline .accent { color: var(--highlight-yellow); }
  .pull-quote {
    position: absolute;
    left: 81px;
    top: 723px;
    width: 593px;
    height: 105px;
    box-sizing: border-box;
    padding: 20px 22px 0 22px;
    margin: 0;
    background: var(--quote-navy);
    font-family: "Roboto", sans-serif;
    font-style: italic;
    font-size: 17px;
    line-height: 23px;
    letter-spacing: 0.6px;
    text-align: right;
    color: var(--text-white);
  }
  .pull-quote strong {
    color: var(--highlight-yellow);
    font-weight: 700;
  }
  .corner-wedge {
    position: absolute;
    left: 0;
    top: 0;
  }
  .imprint {
    position: absolute;
    left: 548px;
    top: 1112px;
    display: flex;
    align-items: center;
    gap: 8px;
    font-family: "Barlow Condensed", sans-serif;
    font-weight: 600;
    font-size: 24px;
    line-height: 24px;
    color: var(--imprint-ink);
  }
  .imprint-mark {
    width: 12px;
    height: 12px;
    background: var(--imprint-ink);
    flex: none;
  }
</style>
</head>
<body>
  <main class="back-cover">
    <svg class="corner-wedge" width="751" height="1200" viewBox="0 0 751 1200" aria-hidden="true">
      <polygon points="751,866 751,1200 437,1200" fill="var(--corner-white)"/>
    </svg>

    <h1 class="headline">
      <span class="line">A book about the</span>
      <span class="line">stock market</span>
      <span class="line accent">for people who</span>
      <span class="line">don't read books</span>
      <span class="line accent">about the stock market.</span>
    </h1>

    <p class="pull-quote">"An easy to follow, easy to read book, outlining a <strong>15 step process to help you make better investing decisions."</strong></p>

    <div class="imprint">
      <span class="imprint-mark"></span>
      <span class="imprint-name">Brookvale Saver<br>Institute</span>
    </div>
  </main>
</body>
</html>
```